A website for Medical Services to treat incontinence with a non-invasive product

We need to build a website to generate and convert new clients to schedule either treatment or book consultation (The device's name is KVR TONARIX). Here are the reference sites for information only: (Please do not use the same style as this is the style we desperately want to change)
http://www.pelvoracare.example/tonarix-for-incontinence/
https://vormidaspa.example/2018/04/13/urinary-incontinence/
https://vormidaspa.example/non-invasive-lasers/female-incontinence/
http://www.drquaven.example/services/wellness-services/sexual-health/kvr-tonarix-urinary-incontinence-houston/

This is the vendor site:
https://corvanthmed.example/

Target Market(s)

The targeted audience is mostly women between 30 - 75, suffering from stress incontinence due to childbirth and many other age-related conditions.

Industry/Entity Type

Health And Wellness

Number of Pages Required

4 page

Font styles to use
Sans Serif

Colors

Designer to choose colors to be used in the design.

Requirements
Must have
• How it works, How is it different from traditional invasive measures, What other people say about the treatment, video testimonials, FAQs, contact us, Book Appointment, latest promotions. maps, social media links
Nice to have
• The experienced urologist profile, office surroundings/interior, Reviews, number strips

```html
<!DOCTYPE html>
<html lang="en">
<head>
<meta charset="utf-8">
<title>Lumeva Clinic – KVR TONARIX</title>
<link href="https://fonts.googleapis.com/css2?family=Roboto+Condensed:wght@400;500;700&family=Questrial&display=swap" rel="stylesheet">
<style>
:root{
  --teal:#7fdbe2;
  --ink:#2f2f2f;
  --grey-text:#555;
  --muted:#9a9a9a;
  --footer:#3b3b3b;
  --beige:#ece7e0;
  --white:#fff;
  --line:#cfcfcf;
}
*{box-sizing:border-box;margin:0;padding:0}
html,body{width:1200px;height:3352px;overflow:hidden}
body{font-family:"Questrial",sans-serif;color:var(--grey-text);background:var(--white);position:relative}
.abs{position:absolute}
.heading{font-family:"Roboto Condensed",sans-serif;font-weight:700;color:var(--ink);text-transform:uppercase;letter-spacing:.5px}
.accent-bar{width:38px;height:3px;background:var(--teal);position:absolute}

/* top bar */
.topbar{top:0;left:0;width:1200px;height:45px;font-size:12px;color:var(--ink)}
.topbar .item{position:absolute;top:14px;display:flex;align-items:center;gap:8px;white-space:nowrap}
.topbar .social{position:absolute;top:8px;right:153px;display:flex;gap:14px}
.topbar .social span{width:26px;height:26px;border:1.5px solid var(--ink);display:block;position:relative}
.topbar .social span::after{content:"";position:absolute;left:8px;top:8px;width:7px;height:7px;background:var(--ink);border-radius:50%}

/* hero */
.hero{top:0;left:0;width:1200px;height:600px;background:linear-gradient(100deg,#f5efe6 0%,#efe7dc 45%,#e3d6c6 70%,#f1ebe3 100%);z-index:-1}
.nav{top:86px;left:161px;width:878px;height:30px}
.wordmark{position:absolute;left:0;top:2px;font-family:"Questrial",sans-serif;font-weight:400;font-size:21px;color:var(--ink);letter-spacing:.5px;white-space:nowrap}
.menu{position:absolute;left:237px;top:6px;display:flex;font-size:12px;color:var(--ink);white-space:nowrap}
.menu li{list-style:none;display:flex}
.menu li+li::before{content:"/";margin:0 16px;color:var(--ink)}
.menu .active{border-bottom:2px solid var(--ink);padding-bottom:4px}
.hero-title{top:230px;left:0;width:1200px;text-align:center;font-family:"Roboto Condensed",sans-serif;font-weight:500;font-size:86px;color:#444;letter-spacing:.5px}
.hero-text{top:342px;left:190px;width:820px;text-align:center;font-size:15px;line-height:26px;color:var(--ink)}
.hero-arrows{top:414px;left:579px;display:flex;gap:4px}
.hero-arrows span{width:19px;height:19px;border-radius:50%;background:var(--ink);display:flex;align-items:center;justify-content:center}

/* appointment */
.booking{top:521px;left:646px;width:393px;height:339px;background:var(--white);box-shadow:0 6px 24px rgba(0,0,0,.14);padding:30px 36px}
.booking h3{font-family:"Roboto Condensed",sans-serif;font-weight:700;font-size:18px;color:var(--ink);text-align:center;text-decoration:underline;text-underline-offset:4px;letter-spacing:.5px}
.field{position:absolute;font-size:11.5px;color:var(--ink);border-bottom:1.5px solid #777;padding-bottom:6px}
.field.msg{height:68px;border-left:1.5px solid #777;padding:6px 0 0 4px}
.submit{position:absolute;left:144px;top:269px;width:104px;height:40px;background:var(--teal);color:var(--white);font-size:11px;display:flex;align-items:center;justify-content:center;letter-spacing:.5px}

/* how it works */
.how{top:680px;left:161px}
.how h2{font-size:23px;margin-top:16px}
.checklist{list-style:none;margin-top:20px}
.checklist li{display:flex;align-items:center;gap:14px;font-size:13px;color:var(--ink);height:32.5px;white-space:nowrap}

/* split band */
.band-left{top:945px;left:0;width:599px;height:458px;background:linear-gradient(135deg,#8ee0e6,#a9e9ec 60%,#98e3e8)}
.band-right{top:945px;left:599px;width:601px;height:458px;background:linear-gradient(135deg,#656565,#555 55%,#5e5e5e)}
.band-title{font-family:"Roboto Condensed",sans-serif;font-size:23px;color:var(--white);text-transform:uppercase;line-height:32px;letter-spacing:.5px}
.band-text{font-size:12px;line-height:22px;color:var(--white)}
.btn-white{position:absolute;width:120px;height:40px;background:var(--white);color:var(--ink);font-size:11px;display:flex;align-items:center;justify-content:center;gap:6px}
.numbered{list-style:none}
.numbered li{display:flex;gap:16px;font-size:12px;line-height:21px;color:var(--white);margin-bottom:22px}
.numbered .num{flex:none;width:24px;height:24px;border-radius:50%;background:var(--white);color:var(--ink);font-weight:700;font-size:13px;display:flex;align-items:center;justify-content:center;margin-top:-1px}

/* product */
.product-media{top:1480px;left:181px;width:438px;height:312px;background:linear-gradient(160deg,#f4f4f4,#e9eeef);box-shadow:0 4px 20px rgba(0,0,0,.08)}
.product-card{top:1504px;left:594px;width:436px;height:318px;background:var(--white);box-shadow:0 6px 24px rgba(0,0,0,.14);padding:44px 60px 0 73px}
.product-card h2{font-size:25px;margin-top:14px}
.product-card p{font-size:11.5px;line-height:22px;color:var(--ink);margin-top:12px}
.btn-teal{position:absolute;width:118px;height:40px;background:var(--teal);color:var(--white);font-size:11px;display:flex;align-items:center;justify-content:center;gap:6px}

/* testimonials */
.testimonials{top:1895px;left:0;width:1200px;height:429px;background:radial-gradient(ellipse at 70% 40%,#f2eee8,var(--beige) 70%)}
.section-title{position:absolute;left:0;width:1200px;text-align:center;font-size:22px}
.video{top:2023px;left:161px;width:411px;height:241px;background:var(--white);padding:5px;box-shadow:0 2px 8px rgba(0,0,0,.1)}
.video .frame{width:100%;height:100%;background:linear-gradient(120deg,#cfe6f2,#a9cde2 55%,#dfeef6)}
.play{position:absolute;left:183px;top:107px;width:36px;height:36px;border-radius:50%;background:#e94a3b}
.avatar{top:2032px;left:653px;width:98px;height:98px;border-radius:50%;background:linear-gradient(135deg,#d9c5b0,#b99d85);border:3px solid var(--white)}
.reviewer{top:2066px;left:778px;font-size:11.5px;color:var(--ink);line-height:20px}
.reviewer strong{font-family:"Roboto Condensed",sans-serif;font-weight:700;font-size:12px;text-transform:uppercase}
.quote{top:2150px;left:653px;width:395px;font-size:12px;line-height:22px;color:var(--ink)}
.dots{top:2242px;left:653px;display:flex;gap:5px}
.dots span{width:7px;height:7px;border-radius:50%;background:var(--teal)}

/* faqs */
.faq{position:absolute;top:2450px;width:284px;height:114px;border:1px solid var(--line);padding:18px 16px}
.faq .q{display:flex;align-items:center;gap:12px;font-family:"Roboto Condensed",sans-serif;font-weight:700;font-size:12.5px;color:var(--ink)}
.faq .icon{width:34px;height:26px;background:var(--teal);display:flex;align-items:center;justify-content:center}
.faq p{font-size:10.5px;line-height:19px;color:var(--muted);margin-top:10px}
.faq .go{position:absolute;right:0;bottom:0;width:22px;height:20px;background:#555;display:flex;align-items:center;justify-content:center}
.pager{top:2596px;left:575px;display:flex;gap:6px}
.pager span{width:14px;height:3px;background:#4a5e78}

/* footer */
.footer{top:2671px;left:0;width:1200px;height:395px;background:var(--footer);color:#bfbfbf;font-size:11.5px}
.f-head{position:absolute;font-family:"Roboto Condensed",sans-serif;font-weight:700;font-size:13px;color:var(--white);text-transform:uppercase;letter-spacing:.4px}
.f-head::after{content:"";position:absolute;left:0;top:24px;width:138px;height:1.5px;background:#8a8a8a}
.f-list{position:absolute;list-style:none;line-height:22.5px}
.social-row{position:absolute;display:flex;align-items:center;gap:16px}
.social-row .ring{width:26px;height:26px;border:1.5px solid #bfbfbf;border-radius:50%}
.newsletter{position:absolute;left:355px;top:128px;width:232px;height:36px;background:var(--white);color:#666;font-size:11px;display:flex;align-items:center;justify-content:space-between;padding:0 12px}
.info-row{position:absolute;display:flex;align-items:center;gap:14px;white-space:nowrap}
.book-btn{position:absolute;left:885px;top:107px;width:153px;height:44px;background:var(--teal);color:var(--white);font-size:12px;display:flex;align-items:center;justify-content:center}

/* map */
.map{top:3066px;left:0;width:1200px;height:237px;background:linear-gradient(135deg,#dcdcdc,#cdcdcd 50%,#d8d8d8)}
.map-card{top:3137px;left:500px;width:207px;height:56px;background:var(--white);font-size:11.5px;line-height:17px;color:var(--ink);text-align:center;padding-top:11px}
.map-close{top:3210px;left:580px;width:40px;height:40px;border-radius:50%;background:#1f1f1f;color:var(--white);font-size:16px;display:flex;align-items:center;justify-content:center}
.copyright{top:3303px;left:0;width:1200px;height:49px;font-size:12px;color:var(--ink)}
</style>
</head>
<body>

<header class="abs topbar">
  <div class="item" style="left:161px">
    <svg width="14" height="14" viewBox="0 0 24 24"><path d="M6.6 10.8a15 15 0 0 0 6.6 6.6l2.2-2.2a1 1 0 0 1 1-.25 11 11 0 0 0 3.6.6 1 1 0 0 1 1 1V20a1 1 0 0 1-1 1A17 17 0 0 1 3 4a1 1 0 0 1 1-1h3.5a1 1 0 0 1 1 1c0 1.25.2 2.45.6 3.6a1 1 0 0 1-.25 1z" fill="#2f2f2f"/></svg>
    <span>Phone &nbsp;|&nbsp; +1 555 0142 886</span>
  </div>
  <div class="item" style="left:340px">
    <svg width="15" height="12" viewBox="0 0 24 18"><rect x="1" y="1" width="22" height="16" fill="none" stroke="#2f2f2f" stroke-width="2"/><path d="M1 1l11 9 11-9" fill="none" stroke="#2f2f2f" stroke-width="2"/></svg>
    <span>Mail : info@lumevaclinic.example</span>
  </div>
  <div class="social"><span></span><span></span><span></span><span></span></div>
</header>

<div class="abs hero" role="img" aria-label="Hero photograph of a smiling woman sitting relaxed at home in soft daylight"></div>

<nav class="abs nav">
  <div class="wordmark">LUMEVA CLINIC</div>
  <ul class="menu">
    <li><span class="active">Home</span></li>
    <li>About</li>
    <li>How it works</li>
    <li>How it is Different</li>
    <li>Testimonials</li>
    <li>FAQs</li>
    <li>Contact Us</li>
  </ul>
</nav>

<h1 class="abs hero-title">Say No To Incontinence</h1>
<p class="abs hero-text">Lorem Ipsum is simply dummy text of the printing and typesetting industry. Lorem Ipsum has been the industry's standard dummy text ever since the 1500s, when an unknown printer took a galley of type</p>
<div class="abs hero-arrows">
  <span><svg width="8" height="8" viewBox="0 0 8 8"><path d="M5.5 1L2.5 4l3 3" stroke="#fff" stroke-width="1.6" fill="none"/></svg></span>
  <span><svg width="8" height="8" viewBox="0 0 8 8"><path d="M2.5 1l3 3-3 3" stroke="#fff" stroke-width="1.6" fill="none"/></svg></span>
</div>

<section class="abs booking">
  <h3>BOOK AN APPOINTMENT</h3>
  <div class="field" style="left:19px;top:88px;width:160px">Name</div>
  <div class="field" style="left:197px;top:88px;width:160px">Phone</div>
  <div class="field" style="left:19px;top:124px;width:338px">E-mail</div>
  <div class="field msg" style="left:19px;top:168px;width:338px">Message</div>
  <div class="submit">SUBMIT</div>
</section>

<section class="abs how">
  <div class="accent-bar" style="top:0;left:0"></div>
  <h2 class="heading">How it works</h2>
  <ul class="checklist">
    <li><svg width="16" height="13" viewBox="0 0 16 13"><path d="M1.5 7l4.5 4.5L14.5 1.5" stroke="var(--teal)" stroke-width="2.4" fill="none"/></svg>Lorem Ipsum is simply dummy text of the printing</li>
    <li><svg width="16" height="13" viewBox="0 0 16 13"><path d="M1.5 7l4.5 4.5L14.5 1.5" stroke="var(--teal)" stroke-width="2.4" fill="none"/></svg>Lorem Ipsum is simply dummy text of the printing</li>
    <li><svg width="16" height="13" viewBox="0 0 16 13"><path d="M1.5 7l4.5 4.5L14.5 1.5" stroke="var(--teal)" stroke-width="2.4" fill="none"/></svg>Lorem Ipsum is simply dummy text of the printing</li>
    <li><svg width="16" height="13" viewBox="0 0 16 13"><path d="M1.5 7l4.5 4.5L14.5 1.5" stroke="var(--teal)" stroke-width="2.4" fill="none"/></svg>Lorem Ipsum is simply dummy text of the printing</li>
    <li><svg width="16" height="13" viewBox="0 0 16 13"><path d="M1.5 7l4.5 4.5L14.5 1.5" stroke="var(--teal)" stroke-width="2.4" fill="none"/></svg>Lorem Ipsum is simply dummy text of the printing</li>
  </ul>
</section>

<section class="abs band-left">
  <div class="accent-bar" style="top:52px;left:161px;background:#fff;opacity:.7"></div>
  <h2 class="band-title abs" style="left:161px;top:60px;width:420px">How is it different from traditio -nal invasive measures</h2>
  <p class="band-text abs" style="left:161px;top:152px;width:395px">Lorem Ipsum is simply dummy text of the printing and typesetting industry. Lorem Ipsum has been the industry's standard dummy text ever since the 1500s, when an unknown printer took a galley of type and scrambled it to make a type specimen book. It has survived...</p>
  <p class="band-text abs" style="left:161px;top:262px;width:395px">Lorem Ipsum is simply dummy text of the printing and typesetting industry. Lorem Ipsum has been the industry's standard dummy text ever since the 1500s, when an unknown printer ...</p>
  <div class="btn-white" style="left:161px;top:365px">Learn More <svg width="6" height="7" viewBox="0 0 6 7"><path d="M0 0l6 3.5L0 7z" fill="#2f2f2f"/></svg></div>
</section>

<section class="abs band-right">
  <div class="accent-bar" style="top:52px;left:49px;background:#fff;opacity:.7"></div>
  <h2 class="band-title abs" style="left:49px;top:60px;width:440px">What other people say about the treatment</h2>
  <ol class="numbered abs" style="left:49px;top:155px;width:400px">
    <li><span class="num">1</span><span>Lorem Ipsum is simply dummy text of the printing and type-setting industry. Lorem Ipsum has been the industry's</span></li>
    <li><span class="num">2</span><span>Lorem Ipsum is simply dummy text of the printing and type-setting industry. Lorem Ipsum has been the industry's</span></li>
    <li><span class="num">3</span><span>Lorem Ipsum is simply dummy text of the printing and type-setting industry. Lorem Ipsum has been the industry's</span></li>
  </ol>
  <div class="btn-white" style="left:53px;top:365px">Learn More <svg width="6" height="7" viewBox="0 0 6 7"><path d="M0 0l6 3.5L0 7z" fill="#2f2f2f"/></svg></div>
</section>

<div class="abs product-media" role="img" aria-label="Product photograph of the KVR TONARIX treatment chair with its control console on wheels"></div>
<section class="abs product-card">
  <div class="accent-bar" style="top:38px;left:73px"></div>
  <h2 class="heading">KVR TONARIX</h2>
  <p>Lorem Ipsum is simply dummy text of the printing and type-setting industry. Lorem Ipsum has been the industry's standard dummy text ever since the 1500s, when an unknown printer took a galley of type and scrambled it to make a type specimen book. It has survived not only five centuries, but also the leap...</p>
  <div class="btn-teal" style="left:73px;top:252px">Learn More <svg width="6" height="7" viewBox="0 0 6 7"><path d="M0 0l6 3.5L0 7z" fill="#fff"/></svg></div>
</section>

<section class="abs testimonials">
  <h2 class="heading section-title" style="top:70px">Testimonials</h2>
</section>
<div class="abs video">
  <div class="frame" role="img" aria-label="Video testimonial still of a patient and her doctor in the clinic"></div>
  <div class="play"><svg width="36" height="36" viewBox="0 0 36 36"><path d="M14 11l11 7-11 7z" fill="#fff"/></svg></div>
</div>
<div class="abs avatar" role="img" aria-label="Portrait of the reviewer"></div>
<div class="abs reviewer"><strong>Marisa Colden</strong><br>(31-May-2018)</div>
<p class="abs quote">Lorem Ipsum is simply dummy text of the printing and typeset-ting industry. Lorem Ipsum has been the industry's standard dummy text ever since Industry...</p>
<div class="abs dots"><span></span><span></span><span></span></div>

<div class="accent-bar" style="top:2378px;left:581px"></div>
<h2 class="heading section-title" style="top:2392px">FAQs</h2>

<article class="faq" style="left:161px">
  <div class="q"><span class="icon"><svg width="18" height="14" viewBox="0 0 18 14"><rect x="1" y="1" width="12" height="8" rx="2" fill="#fff"/><rect x="6" y="5" width="11" height="7" rx="2" fill="none" stroke="#fff" stroke-width="1.4"/></svg></span>What is TONARIX?</div>
  <p>Lorem Ipsum is simply dummy text of the printing and typesetting industry standard dummy text</p>
  <span class="go"><svg width="10" height="8" viewBox="0 0 10 8"><path d="M0 4h8M5 1l3 3-3 3" stroke="#fff" stroke-width="1.4" fill="none"/></svg></span>
</article>
<article class="faq" style="left:458px">
  <div class="q"><span class="icon"><svg width="18" height="14" viewBox="0 0 18 14"><rect x="1" y="1" width="12" height="8" rx="2" fill="#fff"/><rect x="6" y="5" width="11" height="7" rx="2" fill="none" stroke="#fff" stroke-width="1.4"/></svg></span>Who does TONARIX work for?</div>
  <p>Lorem Ipsum is simply dummy text of the printing and typesetting industry standard dummy text</p>
  <span class="go"><svg width="10" height="8" viewBox="0 0 10 8"><path d="M0 4h8M5 1l3 3-3 3" stroke="#fff" stroke-width="1.4" fill="none"/></svg></span>
</article>
<article class="faq" style="left:755px">
  <div class="q"><span class="icon"><svg width="18" height="14" viewBox="0 0 18 14"><rect x="1" y="1" width="12" height="8" rx="2" fill="#fff"/><rect x="6" y="5" width="11" height="7" rx="2" fill="none" stroke="#fff" stroke-width="1.4"/></svg></span>How does the treatment work?</div>
  <p>Lorem Ipsum is simply dummy text of the printing and typesetting industry standard dummy text</p>
  <span class="go"><svg width="10" height="8" viewBox="0 0 10 8"><path d="M0 4h8M5 1l3 3-3 3" stroke="#fff" stroke-width="1.4" fill="none"/></svg></span>
</article>
<div class="abs pager"><span></span><span></span><span></span></div>

<footer class="abs footer">
  <div class="f-head" style="left:161px;top:55px">Social Link</div>
  <div class="social-row" style="left:161px;top:94px"><span class="ring"></span>Kinnect</div>
  <div class="social-row" style="left:161px;top:128px"><span class="ring"></span>Streamly</div>
  <div class="social-row" style="left:161px;top:162px"><span class="ring"></span>Snapgrid</div>

  <div class="f-head" style="left:355px;top:55px">Stay in Touch</div>
  <div style="position:absolute;left:355px;top:100px">Subscribe to our Newsletter</div>
  <div class="newsletter"><span>Email Address</span><svg width="16" height="14" viewBox="0 0 16 14"><path d="M0 0l16 7-16 7 3-7z" fill="#333"/></svg></div>

  <div class="f-head" style="left:640px;top:55px">Information</div>
  <div class="info-row" style="left:640px;top:104px"><svg width="13" height="13" viewBox="0 0 24 24"><path d="M6.6 10.8a15 15 0 0 0 6.6 6.6l2.2-2.2a1 1 0 0 1 1-.25 11 11 0 0 0 3.6.6 1 1 0 0 1 1 1V20a1 1 0 0 1-1 1A17 17 0 0 1 3 4a1 1 0 0 1 1-1h3.5a1 1 0 0 1 1 1c0 1.25.2 2.45.6 3.6a1 1 0 0 1-.25 1z" fill="#bfbfbf"/></svg>Call Us : +1 555 0142 886</div>
  <div class="info-row" style="left:640px;top:138px"><svg width="13" height="10" viewBox="0 0 24 18"><rect x="1" y="1" width="22" height="16" fill="none" stroke="#bfbfbf" stroke-width="2"/><path d="M1 1l11 9 11-9" fill="none" stroke="#bfbfbf" stroke-width="2"/></svg>info@lumevaclinic.example</div>
  <div class="book-btn">Book Appointment</div>

  <div class="f-head" style="left:161px;top:250px">Navigation</div>
  <ul class="f-list" style="left:161px;top:285px"><li>Home</li><li>About</li><li>How It Works</li><li>How It Is Different</li></ul>
  <ul class="f-list" style="left:427px;top:285px"><li>Testimonials</li><li>FAQs</li><li>Contact Us</li></ul>

  <div class="f-head" style="left:640px;top:250px">Company</div>
  <ul class="f-list" style="left:640px;top:285px"><li>Support</li><li>Customers</li><li>Help</li></ul>
  <ul class="f-list" style="left:927px;top:285px"><li>Login</li><li>Terms and Condition</li></ul>
</footer>

<div class="abs map" role="img" aria-label="Street map showing the clinic location"></div>
<div class="abs map-card">Lorem Ipsum is dummy text<br>printing &amp; industry.</div>
<div class="abs map-close">X</div>

<div class="abs copyright">
  <span style="position:absolute;left:161px;top:17px">© Copyright 2018 Lumeva Clinic. All Rights Reserved.</span>
  <span style="position:absolute;right:161px;top:17px">Privacy Policy</span>
</div>

</body>
</html>
```